LumaCREST new era @ Hyper Digitalization

We need a Brochure that show all our product, services and consulting related to Hyper Digitalization into the industrial internet of things world.
We need a document that can be handled as a electronic brochure, this means that we need to show strong corporate presence, with strong skill of technology, and we have credentials and key sucess projects related to Manufacturing industries.
Key industries that we attend: Automotive, Chemical, Food and Beverage, Mining, Paper and Pulp, Oil and Gas, Energy Management.
We save money to our customer in 6 ways: 1) Eficiency in operation 2) Production Control 3) Hyper Digitalization of Thing Optimizing asset ussage 4) Maintenance and predictive of assets risks 5) Quality Control reducing Cost 6) Augmented Reality in operation and control
Target Market(s)
Manufacturing Industry. CEO of companies that has challenges of saving operation costs into plants of manufacturing.
Industry/Entity Type
Software
Other font styles liked:
- MONTSERRAT
Requirements
Must have
- Technology Enviroment, our logo, our expertise, simple message about what our company does and the DNA, infography of the company, cases of sucess, cases of savings $ using our tecnology and services, what we can do for the customer in a few words
Nice to have
- standarize our colors related to our presentation, futuristic, information related to Artificial Inteligence related to machinery
Should not have
- old version of technology,

```html
<!DOCTYPE html>
<html lang="en">
<head>
<meta charset="utf-8">
<title>LumaCREST — The new era: Optimizing industries @ HyperDigitalization</title>
<link rel="stylesheet" href="https://fonts.googleapis.com/css2?family=Montserrat:wght@300;400;600;700&display=swap">
<style>
  :root {
    --brand-blue: #0a7dbf;
    --navy: #1f4c73;
    --deep-navy: #0b2239;
    --cyan: #00b3e0;
    --ink: #1d2a36;
    --muted: #8a8f96;
    --rule: #b9bcc0;
    --paper: #ffffff;
  }
  * { margin: 0; padding: 0; box-sizing: border-box; }
  html, body { width: 849px; height: 1200px; overflow: hidden; background: var(--paper); }
  body { font-family: "Montserrat", sans-serif; color: var(--ink); }
  .cover { position: relative; width: 849px; height: 1200px; overflow: hidden; }

  .top-band {
    position: absolute; left: 0; top: 0; width: 491px; height: 56px;
    background: linear-gradient(90deg, #087cbd 0%, #0a7fc2 100%);
  }

  .hero-visual {
    position: absolute; left: 0; top: 75px; width: 491px; height: 695px;
    background:
      radial-gradient(ellipse 34% 24% at 50% 66%, rgba(0,190,235,0.95) 0%, rgba(0,170,220,0.55) 55%, rgba(0,170,220,0) 100%),
      radial-gradient(ellipse 62% 46% at 55% 70%, rgba(0,160,215,0.85) 0%, rgba(12,120,180,0.55) 50%, rgba(20,90,140,0) 100%),
      radial-gradient(ellipse 30% 22% at 95% 55%, rgba(0,175,225,0.8) 0%, rgba(0,175,225,0) 100%),
      radial-gradient(ellipse 55% 30% at 70% 38%, rgba(40,140,200,0.45) 0%, rgba(40,140,200,0) 100%),
      radial-gradient(ellipse 35% 25% at 8% 85%, rgba(60,150,210,0.35) 0%, rgba(60,150,210,0) 100%),
      linear-gradient(180deg, #1f4b70 0%, #1f5a85 40%, #1e6a9b 70%, #1d5a88 100%);
  }

  .hero-title {
    position: absolute; right: 509px; top: 218px;
    font-weight: 700; font-size: 29.5px; line-height: 32.5px;
    letter-spacing: -0.6px; color: var(--paper); text-align: right;
  }

  .feature-frame {
    position: absolute; left: 389px; top: 161px; width: 460px; height: 236px;
    background: var(--paper);
  }
  .feature-visual {
    position: absolute; left: 6px; top: 6px; width: 454px; height: 224px;
    background:
      radial-gradient(circle at 25% 51%, #e8fbff 0%, #7fe0fb 5%, #2bb8ea 14%, rgba(20,120,180,0.7) 30%, rgba(12,50,85,0) 52%),
      radial-gradient(ellipse 45% 6% at 72% 50%, rgba(140,215,250,0.9) 0%, rgba(60,160,225,0.4) 55%, rgba(30,110,180,0) 100%),
      radial-gradient(ellipse 17% 42% at 55% 55%, #d8eefa 0%, #9bcbe8 45%, rgba(80,140,190,0) 100%),
      radial-gradient(ellipse 30% 35% at 85% 85%, rgba(30,130,200,0.6) 0%, rgba(20,80,140,0) 100%),
      radial-gradient(ellipse 25% 25% at 90% 25%, rgba(20,90,150,0.5) 0%, rgba(20,90,150,0) 100%),
      linear-gradient(90deg, #0d2b47 0%, #123e62 45%, #0e3253 70%, #0b2239 100%);
  }

  .divider-vertical { position: absolute; left: 490px; top: 770px; width: 1px; height: 127px; background: var(--rule); }

  .brand-name {
    position: absolute; left: 492px; top: 938px;
    font-weight: 600; font-size: 42px; letter-spacing: -0.5px; color: var(--brand-blue);
  }

  .divider-horizontal { position: absolute; left: 493px; top: 1018px; width: 356px; height: 1px; background: var(--rule); }

  .contact-list { position: absolute; left: 493px; top: 1050px; list-style: none; font-size: 14.6px; line-height: 17px; }
  .contact-item { position: relative; padding-left: 29px; margin-bottom: 17px; }
  .contact-item svg { position: absolute; left: 0; top: 1px; width: 16px; height: 16px; fill: var(--brand-blue); }

  .website {
    position: absolute; left: 52px; top: 1131px;
    font-weight: 300; font-size: 18px; letter-spacing: 0.3px; color: var(--muted);
  }
</style>
</head>
<body>
<main class="cover">
  <div class="top-band"></div>

  <div class="hero-visual" role="img" aria-label="Glowing digital globe showing the Americas wrapped in network connection lines and light nodes"></div>

  <h1 class="hero-title">The new era:<br>Optimizing<br>industries @<br>HyperDigitalization</h1>

  <div class="feature-frame">
    <div class="feature-visual" role="img" aria-label="Futuristic artificial intelligence concept with glowing circuitry rings and a beam of light"></div>
  </div>

  <div class="divider-vertical"></div>

  <div class="brand-name">LumaCREST</div>

  <div class="divider-horizontal"></div>

  <ul class="contact-list">
    <li class="contact-item address">
      <svg viewBox="0 0 24 24" aria-hidden="true"><path d="M12 1.5a7.5 7.5 0 0 0-7.5 7.5c0 5.6 7.5 13.5 7.5 13.5s7.5-7.9 7.5-13.5A7.5 7.5 0 0 0 12 1.5zm0 10.2a2.8 2.8 0 1 1 0-5.6 2.8 2.8 0 0 1 0 5.6z"/></svg>
      Monterrey, NL<br>Av. Lumen # 215, Col. Vistaclara
    </li>
    <li class="contact-item email">
      <svg viewBox="0 0 24 24" aria-hidden="true"><path d="M2 5h20v14H2zm2 2v.4l8 5.2 8-5.2V7zm0 2.8V17h16V9.8l-8 5.2z"/></svg>
      contacto@lumacrest-mx.com
    </li>
    <li class="contact-item phone">
      <svg viewBox="0 0 24 24" aria-hidden="true"><path d="M6.6 10.8a15.2 15.2 0 0 0 6.6 6.6l2.2-2.2a1 1 0 0 1 1-.25 11.4 11.4 0 0 0 3.6.57 1 1 0 0 1 1 1V20a1 1 0 0 1-1 1A17 17 0 0 1 3 4a1 1 0 0 1 1-1h3.5a1 1 0 0 1 1 1c0 1.25.2 2.45.57 3.57a1 1 0 0 1-.25 1z"/></svg>
      +52 81 5550 1288
    </li>
  </ul>

  <p class="website">www.lumacrest-mx.com</p>
</main>
</body>
</html>
```